Kem7Dex Letterhead

Need a new letterhead for my law firm.
IDENTIFYING INFORMATION BELOW:
Ansel T Brightwater III
Attorney at Law
Address: 4832 Tillbury Rd, Ste 250, Dallas, TX 75204
Phone: 866-402-7183
Fax: 469-583-0271
Email: kem@kem7dex.example
Website: www.kem7dex.example

Colors
0054AA
0677BA
7BADD7
CADEEF
E8F1F8

Requirements
Must have
• Logo needs to be on the letterhead, along with identifying information which is included in the project description.

```html
<!DOCTYPE html>
<html lang="en">
<head>
<meta charset="utf-8">
<title>Kem7Dex Letterhead</title>
<link href="https://fonts.googleapis.com/css2?family=Open+Sans:wght@400;600;700&display=swap" rel="stylesheet">
<style>
  :root {
    --backdrop: #e4e7ec;
    --paper: #ffffff;
    --ink: #1a1a1a;
    --body-ink: #4a4a4a;
    --muted: #8c8c8c;
    --band-dark: #1c1c1c;
    --band-sky: #1ea0dc;
    --band-blue: #0677ba;
    --signature-tone: #d9dde3;
  }
  * { margin: 0; padding: 0; box-sizing: border-box; }
  html, body {
    width: 1200px; height: 900px; overflow: hidden;
    background: var(--backdrop);
    font-family: "Open Sans", Arial, sans-serif;
  }
  .letterhead {
    position: absolute; left: 270px; top: 23px;
    width: 660px; height: 854px;
    background: var(--paper);
    box-shadow: 0 2px 10px rgba(0,0,0,.12);
  }
  .brand {
    position: absolute; top: 92px; left: 0; right: 0;
    text-align: center;
    font-weight: 700; font-size: 27px; letter-spacing: 2px;
    color: var(--ink);
  }
  .letter-body {
    position: absolute; left: 71px; right: 71px; top: 240px;
    color: var(--body-ink);
  }
  .subject { font-size: 13px; color: var(--ink); margin-bottom: 26px; }
  .paragraph {
    font-size: 8.6px; line-height: 15.7px; text-align: justify;
  }
  .paragraph + .paragraph { margin-top: 15.7px; }
  .sender { position: absolute; left: 71px; top: 570px; }
  .sender-name { font-size: 10px; color: var(--ink); }
  .sender-title { font-size: 8px; color: var(--muted); margin-top: 4px; }
  .signature {
    margin-top: 18px; width: 58px; height: 30px;
    background: var(--signature-tone); border-radius: 3px;
  }
  .contact-row {
    position: absolute; left: 26px; right: 26px; top: 808px;
    display: flex; justify-content: space-between; align-items: flex-start;
    font-size: 7.6px; color: var(--muted); line-height: 11px;
  }
  .contact-item { display: flex; gap: 5px; align-items: flex-start; }
  .contact-item svg { width: 9px; height: 9px; flex: none; margin-top: 1px; fill: var(--muted); }
  .bands { position: absolute; left: 0; bottom: 0; width: 660px; height: 8px; }
</style>
</head>
<body>
  <main class="letterhead">
    <div class="brand">KEM7DEX</div>

    <section class="letter-body">
      <p class="subject">Lorem ipsum</p>
      <p class="paragraph">Lorem ipsum dolor sit amet, consectetuer adipiscing elit, sed diam nonummy nibh euismod tincidunt ut laoreet dolore magna aliquam erat volutpat. Ut wisi enim ad minim veniam, quis nostrud exerci tation ullamcorper suscipit lobortis nisl ut aliquip ex ea commodo consequat. Duis autem vel eum iriure dolor in hendrerit in vulputate velit esse molestie consequat, vel illum dolore eu feugiat nulla facilisis at vero eros et accumsan et iusto odio dignissim qui blandit praesent luptatum zzril delenit augue duis dolore te feugait nulla facilisi.<br>Lorem ipsum dolor sit amet, cons ectetuer adipiscing elit, sed diam nonummy nibh euismod tincidunt ut laoreet dolore magna aliquam erat volutpat. Ut wisi enim ad minim veniam, quis nostrud exerci tation ullamcorper suscipit lobortis nisl ut aliquip ex ea commodo consequat.</p>
      <p class="paragraph">Lorem ipsum dolor sit amet, consectetuer adipiscing elit, sed diam nonummy nibh euismod tincidunt ut laoreet dolore magna aliquam erat volutpat. Ut wisi enim ad minim veniam, quis nostrud exerci tation ullamcorper suscipit lobortis nisl ut aliquip ex ea commodo consequat. Duis autem vel eum iriure dolor in hendrerit in vulputate velit esse molestie consequat, vel illum dolore eu feugiat nulla facilisis at vero eros et accumsan et iusto odio dignissim qui blandit praesent luptatum zzril delenit augue duis dolore te feugait nulla facilisi.<br>Lorem ipsum dolor sit amet, cons ectetuer adipiscing elit, sed diam nonummy nibh euismod tincidunt ut laoreet dolore magna aliquam erat volutpat. Ut wisi enim ad minim veniam, quis nostrud exerci tation ullamcorper suscipit lobortis nisl ut aliquip ex ea commodo consequat.</p>
    </section>

    <section class="sender">
      <p class="sender-name">Ansel T Brightwater III</p>
      <p class="sender-title">Attorney at Law</p>
      <div class="signature" role="img" aria-label="Handwritten signature"></div>
    </section>

    <footer class="contact-row">
      <span class="contact-item">
        <svg viewBox="0 0 24 24"><path d="M6.6 10.8a15 15 0 0 0 6.6 6.6l2.2-2.2a1 1 0 0 1 1-.25 11.4 11.4 0 0 0 3.6.57 1 1 0 0 1 1 1V20a1 1 0 0 1-1 1A17 17 0 0 1 3 4a1 1 0 0 1 1-1h3.5a1 1 0 0 1 1 1c0 1.25.2 2.45.57 3.57a1 1 0 0 1-.25 1z"/></svg>
        866-402-7183
      </span>
      <span class="contact-item">
        <svg viewBox="0 0 24 24"><path d="M2 5h20v14H2zm2 2v.5l8 5 8-5V7l-8 5z"/></svg>
        kem@kem7dex.example
      </span>
      <span class="contact-item">
        <svg viewBox="0 0 24 24"><path d="M12 2a10 10 0 1 0 0 20 10 10 0 0 0 0-20zm0 2c.9 1.2 1.6 2.6 2 4h-4c.4-1.4 1.1-2.8 2-4zM4.3 14a8 8 0 0 1 0-4h3.4a16 16 0 0 0 0 4zm5.7 0a14 14 0 0 1 0-4h4a14 14 0 0 1 0 4zm6.3 0a16 16 0 0 0 0-4h3.4a8 8 0 0 1 0 4zM12 20c-.9-1.2-1.6-2.6-2-4h4c-.4 1.4-1.1 2.8-2 4z"/></svg>
        www.kem7dex.example
      </span>
      <span class="contact-item">
        <svg viewBox="0 0 24 24"><path d="M6 3h9l3 3v4H6zm-3 8h18v8h-3v2H6v-2H3zm5 5v3h8v-3z"/></svg>
        469-583-0271
      </span>
      <span class="contact-item">
        <svg viewBox="0 0 24 24"><path d="M12 2a7 7 0 0 0-7 7c0 5 7 13 7 13s7-8 7-13a7 7 0 0 0-7-7zm0 9.5A2.5 2.5 0 1 1 12 6.5a2.5 2.5 0 0 1 0 5z"/></svg>
        Address: 4832 Tillbury Rd,<br>Ste 250, Dallas, TX 75204
      </span>
    </footer>

    <svg class="bands" viewBox="0 0 660 8" preserveAspectRatio="none" aria-hidden="true">
      <polygon points="0,0 198,0 190,8 0,8" fill="var(--band-dark)"/>
      <polygon points="210,0 436,0 428,8 202,8" fill="var(--band-sky)"/>
      <polygon points="456,0 660,0 660,8 448,8" fill="var(--band-blue)"/>
    </svg>
  </main>
</body>
</html>
```